Expanding National Maid Service Needs Redesign!

We need a redesigned home page for our residential cleaning company. Winner will be recognized as the designer for a brand about to go national within the United States. Winner will also become the first choice to continue working with the company to design at least 15 more pages.

Looking for redesign of homepage and redesign of logo (logo will use the same elements -- just organized differently with horizontal text).

For the design we are looking for a mix between the following websites:
www. legionofsweeps .example
This is our parent site that will be redesigned

www. tidyrangers .example
We really like the top/header having the three steps.
We would like to have the same font (proxima nova) and colors. We like the location and size of the booking form.
Love the section topics and would like to mimic that.

www. brightnestcleaners .example
We really like the clean art and use of colors.
We love the use of b-roll and branded images. Will provide for our website.

The perfect site would have the cleanliness, layout and booking form of Tidy Rangers and the excellent placement and use of branded images and b-roll of Brightnest Cleaners.

Link to branded images and b-roll is attached to the brief in a text file.

Please message me any questions. Good luck to everyone in the project!

Target Market(s)

Male and Female working professionals between the ages of 30-60 years old.

Industry/Entity Type

Cleaning Service

Number of Pages Required

1 page

Font styles to use
Other font styles liked:
• Proxima Nova

Colors
0355a3
add136

Requirements
Must have
• Most of this is covered in the project description.
• Would like to have our logo split up so that the art of the maids remains the same but the "Legion of Sweeps" text is to the right of the art. Looking for it to be a horizontal logo.
• Must use Proxima Nova font.
• Must use our branded images and videos. Feel free to create stills from the video.
Nice to have
• Nice to have, but not expected, is the b-roll edited to work with your design. We would like to see the designers vision of how the video would look with the website.
• Would be nice to have our logo given an updated look. Made horizontal as mentioned in the project description.
Should not have
• Should not feel busy. Should not use different color scheme than that of Tidy Rangers. Should not have non-branded images of maids.

```html
<!DOCTYPE html>
<html lang="en">
<head>
<meta charset="utf-8">
<title>Legion of Sweeps – Eco Friendly Maid Service</title>
<link rel="stylesheet" href="https://fonts.googleapis.com/css2?family=Montserrat:wght@300;400;500;600;700;800&family=Open+Sans:wght@400;600;700&display=swap">
<style>
:root{
  --blue:#0355a3;
  --blue-dark:#024684;
  --green:#add136;
  --ink:#333a40;
  --muted:#6b7278;
  --line:#dcdfe3;
  --pale:#f3f5f7;
  --dark:#2a2c2e;
  --white:#ffffff;
}
*{box-sizing:border-box;margin:0;padding:0}
html,body{width:1200px;height:3614px;overflow:hidden}
body{font-family:"Open Sans",Arial,sans-serif;color:var(--ink);background:var(--white);position:relative}
.page{position:relative;width:1200px;height:3614px}
.abs{position:absolute}
h1,h2,h3,.heading{font-family:"Montserrat",Arial,sans-serif}

/* header */
.site-header{top:0;left:0;width:1200px;height:82px;background:var(--white)}
.brand{left:100px;top:18px;display:flex;align-items:center;gap:12px}
.brand-mark{width:44px;height:44px;background:var(--green)}
.brand-name{font-family:"Montserrat",sans-serif;font-weight:700;font-size:22px;color:var(--blue);line-height:1}
.brand-sub{font-size:10px;color:var(--blue);letter-spacing:2px;margin-top:3px;font-family:"Montserrat",sans-serif;font-weight:700}
.main-nav{right:98px;top:32px;display:flex;gap:28px;font-family:"Montserrat",sans-serif;font-size:12px;font-weight:600;color:#222;text-transform:uppercase}
.main-nav .phone{color:var(--blue);font-weight:700}

/* steps */
.steps{top:82px;left:0;width:1200px;height:29px;background:#e6ebf0;font-family:"Montserrat",sans-serif;font-size:13px;color:#333}
.steps-active{position:absolute;left:0;top:0}
.step{position:absolute;top:5px;display:flex;align-items:center;gap:8px}
.step .num{width:19px;height:19px;border-radius:50%;border:1.5px solid currentColor;display:flex;align-items:center;justify-content:center;font-size:11px}
.step.current{color:var(--white)}

/* hero */
.hero{top:111px;left:0;width:1200px;height:400px;background:linear-gradient(100deg,#1d2124 0%,#3a3b36 45%,#5a5547 70%,#2f3031 100%)}
.hero-copy{left:100px;top:120px;width:560px}
.hero-title{font-weight:800;font-size:37px;line-height:1.05;color:var(--blue);text-transform:uppercase}
.hero-title span{display:block;color:var(--green);font-size:30px;margin-top:6px}
.hero-text{color:var(--white);font-size:14px;line-height:1.5;margin-top:14px;width:470px}
.btn{display:inline-block;font-family:"Montserrat",sans-serif;font-weight:700;text-transform:uppercase;font-size:12px}
.btn-blue{background:var(--blue);color:var(--white);padding:12px 14px;margin-top:14px}

/* booking form */
.booking{left:735px;top:429px;width:366px;height:752px;background:var(--white);box-shadow:0 4px 18px rgba(0,0,0,.18);padding:26px 33px;font-family:"Montserrat",sans-serif;text-align:center}
.booking h2{font-weight:300;font-size:36px;color:#444;text-align:left;margin-bottom:20px}
.field{height:44px;border:1px solid var(--line);display:flex;align-items:center;font-size:13px;color:#999;padding:0 12px;gap:10px;text-align:left}
.label{font-size:12px;font-weight:600;color:#222;margin:20px 0 10px}
.toggle{display:flex;height:46px}
.toggle div{flex:1;display:flex;align-items:center;justify-content:center;font-size:13px;border:1px solid var(--line)}
.toggle .on{background:var(--blue);color:var(--white);border-color:var(--blue)}
.stepper{display:flex;height:44px;border:1px solid var(--line)}
.stepper div{display:flex;align-items:center;justify-content:center;font-size:13px;color:#333}
.stepper .pm{width:42px;color:#666}
.stepper .val{flex:1;border-left:1px solid var(--line);border-right:1px solid var(--line)}
.note{font-size:9px;color:#888;margin:6px 0 14px}
.times{display:flex;align-items:center;gap:10px}
.times .field{flex:1;justify-content:space-between;color:#555}
.times span{font-size:12px;color:#555}
.check{margin:16px 0;font-size:12px;color:#333;display:flex;align-items:center;justify-content:center;gap:8px}
.check i{width:13px;height:13px;border:1px solid #888;display:inline-block;position:relative}
.btn-green{display:block;background:var(--green);color:var(--white);height:44px;line-height:44px;font-size:12px}

/* welcome */
.welcome{top:511px;left:0;width:1200px;height:699px}
.welcome-head{left:96px;top:70px;width:604px;text-align:center}
.eyebrow{font-family:"Montserrat",sans-serif;font-size:12px;font-weight:600;color:#222;letter-spacing:.5px}
.welcome-head h1{font-size:28px;font-weight:800;color:var(--blue);margin-top:8px;text-transform:uppercase}
.welcome-head h1 span,.section-title span{color:var(--green)}
.rule{width:50px;height:2px;background:var(--blue);margin:6px auto 0}
.lead{font-size:20px;color:#555;margin-top:16px}
.feature{width:300px;text-align:center;font-size:13px;line-height:1.6;color:#555}
.feature svg{display:block;margin:0 auto 18px}

/* video band */
.video-band{top:1210px;left:0;width:1200px;height:308px;background:linear-gradient(90deg,#1b1c1d 0%,#3d3a33 50%,#262728 100%)}
.seal{left:132px;top:42px;width:230px;height:230px;border-radius:50%;background:radial-gradient(circle,#f6cf4c 0%,#e8a91d 70%,#c98b10 100%)}
.video{left:704px;top:36px;width:342px;height:234px;background:var(--white);padding:6px}
.video-screen{width:100%;height:100%;background:linear-gradient(135deg,#b4d64a 0%,#8fb52a 100%);position:relative}
.video-title{position:absolute;left:10px;top:8px;color:var(--white);font-size:13px;font-family:"Montserrat",sans-serif}
.play{position:absolute;left:50%;top:50%;transform:translate(-50%,-50%);width:52px;height:36px;background:rgba(0,0,0,.7);border-radius:8px}
.play:after{content:"";position:absolute;left:21px;top:10px;border-left:14px solid #fff;border-top:8px solid transparent;border-bottom:8px solid transparent}

/* services */
.services{top:1518px;left:0;width:1200px;height:592px}
.section-title{font-weight:800;font-size:28px;color:var(--blue);text-transform:uppercase;text-align:center}
.section-sub{font-size:18px;color:#555;text-align:center;margin-top:14px}
.service{width:226px}
.service-img{height:178px}
.service h3{font-family:"Montserrat",sans-serif;font-weight:400;font-size:22px;color:#333;margin:16px 0 8px}
.service p{font-size:13px;line-height:1.45;color:#666}

/* reviews */
.reviews{top:2110px;left:0;width:1200px;height:505px;background:linear-gradient(90deg,#f4f5f6 0%,#f0f1f0 50%,#d9dccd 70%,#c7ccb3 100%)}
.review{left:157px;top:203px;width:494px;height:194px;background:var(--white);border:1px solid #999;border-radius:6px;padding:26px 24px}
.avatar{position:absolute;left:26px;top:-16px;width:52px;height:52px;border-radius:50%;background:#c9b7a3;border:2px solid #fff;box-shadow:0 0 0 1px #bbb}
.review p{font-size:12.5px;line-height:1.5;color:#444;text-align:center;margin-top:6px}
.review .who{position:absolute;right:24px;bottom:34px;font-family:"Montserrat",sans-serif;font-weight:700;color:var(--blue);font-size:15px}
.arrows{position:absolute;left:58px;bottom:30px;display:flex;gap:4px}
.arrows i{width:24px;height:24px;background:#222;position:relative;display:block}

/* featured */
.featured{top:2615px;left:0;width:1200px;height:330px}
.pub{width:226px;height:90px;border:1px solid var(--line);display:flex;align-items:center;justify-content:center;font-family:"Montserrat",sans-serif;font-size:20px;font-weight:700;color:#444}

/* charity */
.charity{top:2945px;left:0;width:1200px;height:192px;background:linear-gradient(90deg,#2b2d2c 0%,#3f4a3a 40%,#4e5a43 60%,#2c2f2e 100%)}
.charity h2{position:absolute;left:101px;top:42px;font-family:"Montserrat",sans-serif;font-weight:400;font-size:38px;line-height:1.15;color:var(--white)}
.stat{position:absolute;top:44px;text-align:center;color:var(--white);font-family:"Montserrat",sans-serif}
.stat b{display:block;font-weight:400;font-size:46px}
.stat small{font-size:13px;font-weight:700;text-transform:uppercase;letter-spacing:.5px}

/* footer */
.site-footer{top:3137px;left:0;width:1200px;height:434px;background:#f2f2f2}
.foot-col h3{font-family:"Montserrat",sans-serif;font-size:21px;font-weight:600;color:#222;margin-bottom:18px}
.links{list-style:none;font-size:13px;color:#444}
.links li{margin-bottom:15px;display:flex;align-items:center;gap:12px}
.links li:before{content:"";width:7px;height:7px;border-radius:50%;background:#888}
.contact-row{display:flex;gap:14px;font-size:12px;line-height:1.45;color:#333;margin-bottom:22px}
.contact-row .ico{width:28px;height:28px;border-radius:50%;background:var(--blue);flex:none;display:flex;align-items:center;justify-content:center}
.secure{font-family:"Montserrat",sans-serif;font-weight:700;font-size:14px;color:#222;display:flex;align-items:center;gap:8px;margin:-4px 0 10px 0}
.accept{width:234px;border:1px solid #999;padding:0 12px 12px;text-align:center}
.accept legend{font-size:12px;color:#666;padding:0 6px;letter-spacing:1px}
.cards{display:flex;gap:8px;justify-content:center}
.cards i{width:44px;height:28px;border:1px solid #bbb;background:#fff;display:block}
.price-box{left:759px;top:0;width:342px;height:434px;background:var(--blue);padding:38px 52px;color:var(--white)}
.price-box h3{font-family:"Montserrat",sans-serif;font-size:22px;font-weight:600;margin-bottom:18px}
.price-row{display:flex;gap:18px;font-size:15px;margin-bottom:17px}
.price-row b{color:var(--green);font-weight:400;width:36px}
.btn-book{display:block;margin:10px auto 0;width:164px;background:var(--green);color:var(--white);text-align:center;height:36px;line-height:36px;font-size:12px;font-family:"Montserrat",sans-serif;font-weight:600}
.bottom-bar{top:3571px;left:0;width:1200px;height:43px;background:#2b2b2b;color:#ddd;font-size:12px}
.bottom-bar .copy{position:absolute;left:100px;top:14px}
.follow{position:absolute;right:98px;top:7px;display:flex;align-items:center;gap:8px;font-family:"Montserrat",sans-serif;font-weight:700;font-size:14px;color:#fff}
.follow i{width:29px;height:29px;border:1.5px solid #fff;border-radius:50%;display:block}
</style>
</head>
<body>
<div class="page">

  <header class="site-header abs">
    <div class="brand abs">
      <div class="brand-mark"></div>
      <div>
        <div class="brand-name">Legion of Sweeps</div>
        <div class="brand-sub">ECO FRIENDLY</div>
      </div>
    </div>
    <nav class="main-nav abs">
      <span>Home</span><span>Maid Services</span><span>Gift Cards</span><span>About Us</span><span>Charity</span><span>Contact Us</span><span class="phone">(800) 555-0142</span>
    </nav>
  </header>

  <div class="steps abs">
    <svg class="steps-active" width="480" height="29" viewBox="0 0 480 29"><polygon points="0,0 466,0 480,14.5 466,29 0,29" fill="#0355a3"/></svg>
    <div class="step current" style="left:292px"><span class="num">1</span>Cleaning</div>
    <div class="step" style="left:530px"><span class="num">2</span>Pricing/Availability</div>
    <div class="step" style="left:830px"><span class="num">3</span>Done!</div>
  </div>

  <section class="hero abs" role="img" aria-label="Photo of a uniformed maid wiping a kitchen counter with eco-friendly products">
    <div class="hero-copy abs">
      <h1 class="hero-title">Super Maid Service With<span>Eco Friendly Products</span></h1>
      <p class="hero-text">Green House Cleaning Services are the heart of what we do. Brightnest Cleaners is all about making your life Better, Greener, &amp; Cleaner.</p>
      <span class="btn btn-blue">Get Instant Price</span>
    </div>
  </section>

  <section class="welcome abs">
    <div class="welcome-head abs">
      <div class="eyebrow">WELCOME TO OUR SITE</div>
      <h1>Legion of Sweeps <span>Eco Friendly</span></h1>
      <div class="rule"></div>
      <p class="lead">Fighting the war on dirt with eco-friendly weapons.</p>
    </div>

    <div class="feature abs" style="left:96px;top:270px">
      <svg width="70" height="70" viewBox="0 0 70 70" fill="none" stroke="#0355a3" stroke-width="3"><path d="M8 34 L35 10 L62 34"/><rect x="16" y="30" width="38" height="30" fill="#add136"/><rect x="29" y="42" width="12" height="18" fill="#fff"/></svg>
      Your Friends &amp; Family Will Love How Clean You Home Looks &amp; Smells!
    </div>
    <div class="feature abs" style="left:400px;top:270px">
      <svg width="70" height="70" viewBox="0 0 70 70" fill="none" stroke="#0355a3" stroke-width="3"><path d="M14 30 H52 V44 a14 14 0 0 1 -14 14 H28 a14 14 0 0 1 -14 -14 Z" fill="#add136"/><path d="M52 34 h6 a6 6 0 0 1 0 12 h-6"/><path d="M26 12 q4 5 0 10 M35 10 q4 5 0 10 M44 12 q4 5 0 10"/><line x1="10" y1="62" x2="58" y2="62"/></svg>
      Let us handle the cleaning so you can have more free time.
    </div>
    <div class="feature abs" style="left:96px;top:485px">
      <svg width="70" height="70" viewBox="0 0 70 70" fill="none" stroke="#0355a3" stroke-width="3"><rect x="10" y="18" width="50" height="38" rx="4" fill="#add136"/><rect x="38" y="30" width="22" height="14" fill="#fff"/><circle cx="46" cy="37" r="2" fill="#0355a3"/></svg>
      Legion of Sweeps is super flexible &amp; affordable.
    </div>
    <div class="feature abs" style="left:400px;top:485px">
      <svg width="70" height="70" viewBox="0 0 70 70"><circle cx="35" cy="35" r="28" fill="#add136" stroke="#0355a3" stroke-width="3"/><circle cx="35" cy="35" r="18" fill="none" stroke="#0355a3" stroke-width="2"/></svg>
      Backed by our unique 200% Guarantee. You have nothing to lose.
    </div>
  </section>

  <form class="booking abs" aria-label="Get a price">
    <h2>Get a Price</h2>
    <div class="field"><svg width="14" height="14" viewBox="0 0 14 14"><circle cx="7" cy="5" r="3" fill="#bbb"/><path d="M1 14 a6 6 0 0 1 12 0" fill="#bbb"/></svg>Zip Code</div>
    <div class="label">Cleaning Style</div>
    <div class="toggle"><div class="on">Flat Rate</div><div>Hourly</div></div>
    <div class="label">Tell us about your home</div>
    <div class="stepper"><div class="pm">−</div><div class="val">2 bedrooms</div><div class="pm">+</div></div>
    <div class="note">(living room &amp; kitchen included)</div>
    <div class="stepper"><div class="pm">−</div><div class="val">2 bathrooms</div><div class="pm">+</div></div>
    <div class="note">(round half baths up)</div>
    <div class="label" style="margin-top:4px">When would you like us to come?</div>
    <div class="field" style="color:#555"><svg width="16" height="16" viewBox="0 0 16 16" fill="none" stroke="#999"><rect x="1.5" y="3" width="13" height="11.5"/><line x1="1.5" y1="6.5" x2="14.5" y2="6.5"/></svg>12/23/2016</div>
    <div class="label">Any time between</div>
    <div class="times"><div class="field">9:00 AM <span>▾</span></div><span>and</span><div class="field">11:00 AM <span>▾</span></div></div>
    <div class="check"><i></i>I'm flexible</div>
    <span class="btn btn-green">Get Instant Price</span>
  </form>

  <section class="video-band abs" role="img" aria-label="Photo of a maid dusting framed pictures on a wall">
    <div class="seal abs" role="img" aria-label="Satisfaction guarantee seal"></div>
    <svg class="abs" style="left:390px;top:100px" width="290" height="90" viewBox="0 0 290 90" fill="none" stroke="#fff" stroke-width="6" stroke-linecap="round"><path d="M6 70 Q140 0 270 44"/><path d="M244 26 L272 45 L244 64"/></svg>
    <div class="video abs">
      <div class="video-screen" role="img" aria-label="Animated explainer video still showing a cartoon maid">
        <span class="video-title">LegionOfSweeps</span>
        <span class="play"></span>
      </div>
    </div>
  </section>

  <section class="services abs">
    <div class="abs" style="left:0;top:66px;width:1200px">
      <h2 class="section-title">Maid <span>Services</span></h2>
      <div class="rule"></div>
      <p class="section-sub">Flat-rate prices, Guaranteed.</p>
    </div>
    <article class="service abs" style="left:96px;top:198px">
      <div class="service-img" role="img" aria-label="Maid cleaning a bathroom sink" style="background:linear-gradient(135deg,#d9c9ad,#8e9a5e)"></div>
      <h3>Wet Areas</h3>
      <p>Lorem ipsum dolor sit amet, consectetuer adipiscing elit, sed diam nonummy nibh euismod tincidunt ut laoreet dolore magna aliquam erat volutpat.</p>
    </article>
    <article class="service abs" style="left:357px;top:198px">
      <div class="service-img" role="img" aria-label="Two maids cleaning a kitchen" style="background:linear-gradient(135deg,#5b5550,#a2b06a)"></div>
      <h3>Kitchen</h3>
      <p>Lorem ipsum dolor sit amet, consectetuer adipiscing elit, sed diam nonummy nibh euismod tincidunt ut laoreet dolore magna aliquam erat volutpat.</p>
    </article>
    <article class="service abs" style="left:617px;top:198px">
      <div class="service-img" role="img" aria-label="Maid scrubbing a bathroom" style="background:linear-gradient(135deg,#e2ddd4,#9fae62)"></div>
      <h3>Bathroom(s)</h3>
      <p>Lorem ipsum dolor sit amet, consectetuer adipiscing elit, sed diam nonummy nibh euismod tincidunt ut laoreet dolore magna aliquam erat volutpat.</p>
    </article>
    <article class="service abs" style="left:877px;top:198px">
      <div class="service-img" role="img" aria-label="Maid dusting picture frames in a living room" style="background:linear-gradient(135deg,#c9c4bb,#7c8f55)"></div>
      <h3>Living Areas</h3>
      <p>Lorem ipsum dolor sit amet, consectetuer adipiscing elit, sed diam nonummy nibh euismod tincidunt ut laoreet dolore magna aliquam erat volutpat.</p>
    </article>
  </section>

  <section class="reviews abs" role="img" aria-label="Faded photo of a smiling maid wiping a table">
    <div class="abs" style="left:0;top:70px;width:1200px;margin-left:-300px">
      <h2 class="section-title">Customer <span>Reviews</span></h2>
      <div class="rule"></div>
      <p class="section-sub" style="font-size:17px">What Others Are Saying About Us</p>
    </div>
    <div class="review abs">
      <div class="avatar" role="img" aria-label="Customer portrait"></div>
      <p>Marcus, I just wanted to thank you for your help in getting my house ready for showing! Within a week of your team cleaning it well, I got an excellent offer and will be closing on the sale in 2 weeks!! You guys are the best!! Thank you!</p>
      <div class="arrows">
        <i><svg width="24" height="24" viewBox="0 0 24 24"><path d="M14 7 L9 12 L14 17" stroke="#fff" stroke-width="2" fill="none"/></svg></i>
        <i><svg width="24" height="24" viewBox="0 0 24 24"><path d="M10 7 L15 12 L10 17" stroke="#fff" stroke-width="2" fill="none"/></svg></i>
      </div>
      <div class="who">Dana Whitfield</div>
    </div>
  </section>

  <section class="featured abs">
    <div class="abs" style="left:0;top:44px;width:1200px">
      <h2 class="section-title">We Have Been Featured <span>In These Publications</span></h2>
      <div class="rule"></div>
      <p class="section-sub">Lorem ipsum dolor sit amet, consectetuer adipiscing elit</p>
    </div>
    <div class="pub abs" style="left:96px;top:164px">Harbor Sentinel</div>
    <div class="pub abs" style="left:357px;top:164px">Lakeside Weekly</div>
    <div class="pub abs" style="left:617px;top:164px">verdant living</div>
    <div class="pub abs" style="left:877px;top:164px">tidewater</div>
  </section>

  <section class="charity abs" role="img" aria-label="Blurred photo of children sharing a meal">
    <h2>Feeding A Child,<br>Every Time We Clean.</h2>
    <div class="stat" style="left:650px"><b>$ 1,275</b><small>Amount Donated</small></div>
    <div class="stat" style="left:924px"><b>425</b><small>Children Fed</small></div>
  </section>

  <footer class="site-footer abs">
    <div class="foot-col abs" style="left:100px;top:38px">
      <h3>Get in Touch</h3>
      <ul class="links"><li>FAQ</li><li>Blog</li><li>Privacy Policy</li><li>Terms of Service</li><li>Jobs</li><li>Log In</li><li>Sitemap</li></ul>
    </div>
    <div class="foot-col abs" style="left:415px;top:38px">
      <h3>Get in Touch</h3>
      <div class="contact-row"><span class="ico"><svg width="12" height="16" viewBox="0 0 12 16"><path d="M6 0 a6 6 0 0 1 6 6 c0 4 -6 10 -6 10 S0 10 0 6 a6 6 0 0 1 6 -6z" fill="#fff"/><circle cx="6" cy="6" r="2" fill="#0355a3"/></svg></span><div>Legion of Sweeps<br>418 Maple Grove Avenue<br>Springfield, FL 32000</div></div>
      <div class="contact-row"><span class="ico"><svg width="14" height="14" viewBox="0 0 14 14"><path d="M3 1 l2 3 -1.5 1.5 c1 2 2.5 3.5 4.5 4.5 L9.5 8.5 l3 2 -1.5 2.5 C6 13 1 8 1 2.5z" fill="#fff"/></svg></span><div>CALL US :<br>1800 555 0199</div></div>
      <div class="contact-row"><span class="ico"><svg width="14" height="10" viewBox="0 0 14 10"><rect width="14" height="10" fill="#fff"/><path d="M0 0 L7 6 L14 0" stroke="#0355a3" fill="none"/></svg></span><div>EMAIL US :<br>1800 555 0199</div></div>
      <div class="secure"><svg width="14" height="16" viewBox="0 0 14 16"><path d="M3 7 V4.5 a4 4 0 0 1 8 0 V7" stroke="#222" stroke-width="2" fill="none"/><rect y="7" width="14" height="9" fill="#222"/></svg>256-bit encryption</div>
      <fieldset class="accept"><legend>WE ACCEPT</legend><div class="cards"><i></i><i></i><i></i><i></i></div></fieldset>
    </div>
    <div class="price-box abs">
      <h3>Prices Start At</h3>
      <div class="price-row"><b>$85</b>One Bedroom Home</div>
      <div class="price-row"><b>$90</b>Two Bedroom Home</div>
      <div class="price-row"><b>$105</b>Three Bedroom Home</div>
      <div class="price-row"><b>$120</b>Four Bedroom Home</div>
      <div class="price-row"><b>$150</b>Five Bedroom Home</div>
      <div class="price-row"><b>$200</b>Six Bedroom Home</div>
      <span class="btn-book">Book Now</span>
    </div>
  </footer>

  <div class="bottom-bar abs">
    <span class="copy">Copyright © 2017 Legion of Sweeps eco friendly. All Rights Reserved.</span>
    <div class="follow">Follow Us <i></i><i></i><i></i><i></i></div>
  </div>

</div>
</body>
</html>
```